Veterinary Clinic Letterhead - Ridgeview Veterinary Surgery

We need a letterhead design for an established Veterinary Clinic in Mareeba called Ridgeview Veterinary Surgery. We are a moderate sized mixed animal veterinary clinic offering a wide variety of veterinary services. The design should use the same colour pattern as those in the logos supplied. The design should also include our address (48 Tulloch Road, Tolga, Queensland, 4882), phone number (07 4158 6734), email (admin@ridgeviewvets.com.au), website (www.ridgeviewvets.com.au) and our opening hours (8am to 5pm Monday to Friday and 8am to 12pm Saturday).
Target Market(s)
Pet owners
Industry/Entity Type
Veterinary
Requirements
Must have
- The logo or modification of it, business address, opening hours, website, phone number and email address

```html
<!DOCTYPE html>
<html lang="en">
<head>
<meta charset="utf-8">
<title>Ridgeview Veterinary Surgery – Letterhead</title>
<link href="https://fonts.googleapis.com/css2?family=Arimo:wght@400;700&family=Questrial&display=swap" rel="stylesheet">
<style>
  :root {
    --navy: #002b4e;
    --ink-dark: #00121f;
    --paper: #f6f6f7;
    --backdrop: #d9d9d9;
    --text: #555555;
    --text-dark: #2b2b2b;
    --rule: #4f4f4f;
  }
  * { margin: 0; padding: 0; box-sizing: border-box; }
  html, body { width: 1200px; height: 1200px; overflow: hidden; }
  body {
    background: var(--backdrop);
    font-family: "Arimo", Arial, sans-serif;
    color: var(--text);
    position: relative;
  }
  .letterhead {
    position: absolute;
    left: 197px; top: 30px;
    width: 806px; height: 1140px;
    background: var(--paper);
    overflow: hidden;
  }
  .brand {
    position: absolute;
    left: 71px; top: 66px;
    width: 180px;
    display: flex; flex-direction: column; align-items: center; gap: 10px;
  }
  .brand-dot {
    width: 62px; height: 62px; border-radius: 50%;
    background: var(--navy);
  }
  .brand-name {
    font-family: "Arimo", Arial, sans-serif;
    font-weight: 700; font-size: 13px; line-height: 1.25;
    color: var(--navy); text-align: center; text-transform: uppercase;
    letter-spacing: 0.3px;
  }
  .hours {
    position: absolute;
    right: 274px; top: 74px;
    text-align: right; font-size: 11.5px; line-height: 18px;
  }
  .hours-title { color: var(--navy); font-weight: 700; font-size: 12px; }
  .divider {
    position: absolute; left: 547px; top: 62px;
    width: 1px; height: 77px; background: var(--navy);
  }
  .contact {
    position: absolute; left: 562px; top: 61px;
    list-style: none; font-size: 11.5px; line-height: 14.5px; color: var(--text-dark);
  }
  .contact li { display: flex; gap: 6px; align-items: flex-start; }
  .contact .gap { margin-top: 6px; }
  .contact svg { width: 10px; height: 10px; margin-top: 2px; flex: none; fill: var(--navy); }
  .salutation {
    position: absolute; left: 72px; top: 350px;
    font-family: "Questrial", "Century Gothic", sans-serif;
    font-size: 20px; color: var(--text); font-weight: 700;
  }
  .body-copy {
    position: absolute; left: 71px; top: 405px; width: 660px;
    font-size: 13.6px; line-height: 16.6px; color: var(--text);
  }
  .body-copy p + p { margin-top: 14px; }
  .closing {
    position: absolute; left: 72px; top: 745px;
    font-family: "Questrial", sans-serif; font-size: 11px; font-weight: 700; color: var(--text);
  }
  .signature {
    position: absolute; left: 71px; top: 790px;
    width: 134px; height: 42px;
    background: linear-gradient(90deg, #e6e6e8, #dcdcdf);
    border-radius: 4px;
  }
  .footer-band { position: absolute; left: 0; bottom: 0; width: 806px; height: 120px; }
</style>
</head>
<body>
  <main class="letterhead">
    <div class="brand">
      <span class="brand-dot"></span>
      <span class="brand-name">Ridgeview Veterinary Surgery</span>
    </div>

    <div class="hours">
      <div class="hours-title">Our Opening Hours</div>
      <div>8am to 5pm Monday to Friday</div>
      <div>8am to 12pm Saturday</div>
    </div>

    <span class="divider"></span>

    <ul class="contact">
      <li>
        <svg viewBox="0 0 10 10"><path d="M5 0a3.5 3.5 0 0 0-3.5 3.5C1.5 6 5 10 5 10s3.5-4 3.5-6.5A3.5 3.5 0 0 0 5 0zm0 5a1.4 1.4 0 1 1 0-2.8A1.4 1.4 0 0 1 5 5z"/></svg>
        <span>48 Tulloch Road<br>Tolga, Queensland, 4882</span>
      </li>
      <li class="gap">
        <svg viewBox="0 0 10 10"><path d="M2 0.5l1.6 2.2-1 1c.6 1.4 1.6 2.4 3 3l1-1L8.8 7.2 8 9.3C4 9 1 6 .7 2z"/></svg>
        <span>07 4158 6734</span>
      </li>
      <li>
        <svg viewBox="0 0 10 10"><path d="M0 2h10v6H0zM0 2l5 3.5L10 2" stroke="#f6f6f7" stroke-width=".8"/></svg>
        <span>admin@ridgeviewvets.com.au</span>
      </li>
      <li>
        <svg viewBox="0 0 10 10"><circle cx="5" cy="5" r="4.5"/><path d="M.5 5h9M5 .5c-2 2.5-2 6.5 0 9M5 .5c2 2.5 2 6.5 0 9" stroke="#f6f6f7" stroke-width=".7" fill="none"/></svg>
        <span>www.ridgeviewvets.com.au</span>
      </li>
    </ul>

    <h1 class="salutation">Dear Mr. Hartley,</h1>

    <section class="body-copy">
      <p>Lorem ipsum dolor sit amet, consectetuer adipiscing elit, sed diam nonmmy nibh euismod tincidunt ut laor eet dolore magna aliquam erat volutpat. Ut wisi enim ad minim veniam, quis nostrud exerci tationmcorper suscipit lobortis nisl ut aliquip ex ea commodo consequat. Duis autem vel eum iriure dolor in hendrerit in vulputate velit esse molestie consequat, vel illum dolore eu feugiat</p>
      <p>Rorem ipsum dolor sit amet, consectetuer adipiscing elit, sed diam nonmmy nibh euismod tincidunt ut laor eet dolore magna aliquam erat volutpat. Ut wisi enim ad minim veniam, quis nostrud exerci tationmcorper suscipit lobortis nisl ut aliquip ex ea commodo consequat. Duis autem vel eum iriure dolor in hendrerit in vulputate velit esse molest</p>
      <p>Dorem ipsum dolor sit amet, consectetuer adipiscing elit, sed diam nonmmy nibh euismod tincidunt ut laor eet dolore magna aliquam erat volutpat. Ut wisi enim ad minim veniam, quis nostrud exerci tationmcorper suscipit lobortis nisl ut aliquip ex ea commodo consequat. Duis autem vel eum iriure dolor in hendrerit in suscipit lobortis nisl ut aliquip ex ea commodo consequat. Duis autem vel eum iriure dolor in hendrerit in vulputate velit esse molestie consequat, vel illum</p>
      <p>Sorem ipsum dolor sit amet, consectetuer adipiscing elit, sed diam nonmmy nibh euismod tincidunt ut laor eet dolore magna aliquam erat volutpat. Ut wisi enim ad minim veniam, quis nostrud exerci tationmcorper suscipit lobortis nisl ut aliquip ex ea commodo consequat. Duis autem vel eum iriure dolor in</p>
    </section>

    <div class="closing">Sincerely,</div>
    <div class="signature" role="img" aria-label="Handwritten signature of the sender"></div>

    <svg class="footer-band" viewBox="0 0 806 120" preserveAspectRatio="none" aria-hidden="true">
      <path fill="var(--navy)" d="M0 80 C200 40 500 110 806 50 L806 120 L0 120 Z"/>
      <path fill="var(--ink-dark)" d="M520 120 C620 100 720 85 806 80 L806 120 Z"/>
      <path fill="none" stroke="var(--rule)" stroke-width="1.5" d="M0 66 C220 26 500 96 806 36"/>
    </svg>
  </main>
</body>
</html>
```